この度、桜川ベイテラスのレストランのインテリアとして作品を起用されている書道家(前衛・スタイリッシュなスタイル)の作品集を制作する事になりその表紙のデザインをお願いします。
柚木朔香(←作家名)、作品集、2(←第2弾の意味で)、2007-2011)
シンプル 複雑
単色 カラフル
暗い 明るい
日常 高級
遊び心 厳粛
未来的 伝統的
女性的 男性的
特にない (表紙に入れる作品が黒墨なので単調にならないように)
• 高解像度JPG (.jpg)
• イラストレーター形式 (.ai)
• フォトショップ形式 (.psd)
• PNG形式 (.png)
サイズの詳細です
A4 (縦303mm×横215mm, 背幅9mm)
※カバー(袖付き)にする可能性もあるので横幅に関しては、左右3cm前後はみ出したデザインでも良い(袖は140mm)

記載する内容は新たに
Sakuka Yuzuki(←作家名)
KAZE Brush Pages Ⅱ
2007-2011
の3つを加えて下さい
サイズの詳細です
A4 (縦303mm×横215mm, 背幅9mm)
※カバー付きにする可能性もあるので横幅に関しては、袖側に3cm前後はみ出したデザインでも良い(袖は140mm)

記載する内容は新たに
Sakuka Yuzuki(←作家名)
KAZE Brush Pages Ⅱ
の2つを加えて下さい

墨の特徴を端的に表し、それでいて、品格も兼ね備えたシンプルな構成が気に入りました。作品集自体への興味をそそらせる演出となった点が起用した点です。

たくさんのご提案 本当にありがとうごいました。
こちらへの依頼は初めてでしたが色々と勉強になりました。
また、何かございましたら宜しくお願い致します。

```html
<!DOCTYPE html>
<html lang="ja">
<head>
<meta charset="utf-8">
<title>柚木朔香 作品集Ⅱ</title>
<link rel="stylesheet" href="https://fonts.googleapis.com/css2?family=Cormorant+Garamond:ital,wght@1,600&family=Shippori+Mincho+B1:wght@700&display=swap">
<style>
  :root {
    --paper: #f2f2ef;
    --paper-shade: #e6e6e2;
    --label: #e2d6a8;
    --accent: #9a1f1c;
    --ink: #141414;
    --seal: #b0271f;
  }
  * { margin: 0; padding: 0; box-sizing: border-box; }
  html, body { width: 850px; height: 1200px; overflow: hidden; }
  body { background: var(--paper); }
  .cover {
    position: relative;
    width: 850px;
    height: 1200px;
    overflow: hidden;
    background: radial-gradient(ellipse at 50% 45%, var(--paper) 55%, var(--paper-shade) 100%);
  }

  /* calligraphy artwork area */
  .artwork {
    position: absolute;
    left: 340px;
    top: 100px;
    width: 150px;
    height: 990px;
    background: linear-gradient(90deg,
      rgba(20,20,20,0) 0%,
      rgba(20,20,20,0.75) 25%,
      var(--ink) 50%,
      rgba(20,20,20,0.75) 75%,
      rgba(20,20,20,0) 100%);
  }

  /* artist name block, top right */
  .artist-name-en {
    position: absolute;
    left: 547px;
    top: 34px;
    width: 155px;
    height: 74px;
    background: var(--label);
    display: flex;
    align-items: center;
    justify-content: center;
    font-family: "Cormorant Garamond", serif;
    font-style: italic;
    font-weight: 600;
    font-size: 27px;
    color: var(--accent);
    white-space: nowrap;
  }
  .artist-name-ja {
    position: absolute;
    left: 702px;
    top: 34px;
    width: 100px;
    height: 276px;
    background: var(--label);
    writing-mode: vertical-rl;
    display: flex;
    align-items: center;
    justify-content: center;
    font-family: "Shippori Mincho B1", serif;
    font-weight: 700;
    font-size: 52px;
    letter-spacing: 6px;
    color: var(--ink);
  }

  /* collection title block, bottom left */
  .collection-title {
    position: absolute;
    left: 56px;
    top: 892px;
    writing-mode: vertical-rl;
    font-family: "Shippori Mincho B1", serif;
    font-weight: 700;
    font-size: 38px;
    line-height: 44px;
    letter-spacing: 4px;
    color: var(--ink);
  }
  .seal {
    position: absolute;
    left: 110px;
    top: 992px;
    width: 20px;
    height: 20px;
    background: var(--seal);
  }
  .period {
    position: absolute;
    left: 52px;
    top: 1068px;
    font-family: "Cormorant Garamond", serif;
    font-style: italic;
    font-weight: 600;
    font-size: 18px;
    line-height: 20px;
    color: var(--ink);
  }
  .series-title {
    position: absolute;
    left: 42px;
    top: 1114px;
    padding: 6px 14px;
    background: var(--label);
    font-family: "Cormorant Garamond", serif;
    font-style: italic;
    font-weight: 600;
    font-size: 28px;
    line-height: 36px;
    color: var(--accent);
    white-space: nowrap;
  }
</style>
</head>
<body>
  <main class="cover">
    <div class="artwork" role="img" aria-label="黒墨による前衛書の作品：太い縦画と細い左右の払い"></div>

    <div class="artist-name-en">Sakuka Yuzuki</div>
    <div class="artist-name-ja">柚木朔香</div>

    <div class="collection-title">作品集Ⅱ</div>
    <div class="seal" aria-hidden="true"></div>
    <div class="period">2007<br>2011</div>
    <div class="series-title">KAZE Brush Pages Ⅱ</div>
  </main>
</body>
</html>
```